2026 Marwick Dust Control Municipal Advertisement

I need a professional print advertisement designed for our road dust control business for a 2026 municipal/public works publication.

Our company manufactures, supplies, delivers and applies liquid road dust suppressant products to municipalities, contractors and commercial customers across Ontario.

I will upload:

* Our new truck/application photo to use as the main image
* Our advertisement from last year as a reference for the general style and information

I would like the new advertisement to look modern, professional, industrial and appropriate for municipal/public works decision-makers. The truck photo should be the main visual.

Please include the following wording:

MARWICK DUST CONTROL PRODUCTS
418307 Ontario Limited
Based in Clinton, Ontario

ROAD DUST CONTROL PRODUCTS

Manufacturer & Distributor of Liquid Road Dust Suppressants

AVAILABLE CONCENTRATIONS

35%
Liquid Calcium Magnesium Chloride Solution

30%

20%

Bulk Supply • Delivery • Road Application

Supplying Municipalities, Contractors & Commercial Customers Across Ontario

519-555-0187
dermarw417@quillpost.net

Please make “ROAD DUST CONTROL PRODUCTS” one of the most prominent pieces of wording.

The 35%, 30% and 20% product concentrations should also be large, clear and easy to read.

“MARWICK DUST CONTROL PRODUCTS” should be prominently branded, with “418307 Ontario Limited” smaller underneath.

Please do not overcrowd the advertisement. It should be easy for someone flipping through a municipal publication to understand within a few seconds what we sell and how to contact us.

```html
<!DOCTYPE html>
<html lang="en">
<head>
<meta charset="utf-8">
<title>Marwick Dust Control Products — Municipal Advertisement 2026</title>
<link rel="stylesheet" href="https://fonts.googleapis.com/css2?family=Anton&family=Archivo:wdth,wght@125,900&family=Montserrat:wght@500;600;700&family=Oswald:wght@600;700&display=swap">
<style>
:root{
  --navy:#0b1a36;
  --navy-deep:#081429;
  --navy-mid:#1c3560;
  --gold:#f0b323;
  --white:#ffffff;
  --panel:#eceeef;
  --ink:#12203d;
  --sky:#9cc3e6;
  --field:#5d7f3a;
  --road:#8d8676;
}
*{margin:0;padding:0;box-sizing:border-box}
html,body{width:928px;height:1200px;overflow:hidden;background:var(--navy)}
.ad{position:relative;width:928px;height:1200px;background:var(--navy);color:var(--white);font-family:"Montserrat",sans-serif;overflow:hidden}

.header{position:absolute;left:0;top:0;width:928px;height:181px;background:var(--navy);z-index:3}
.header-corner{position:absolute;right:0;top:0}
.brand-mark{position:absolute;left:58px;top:42px;width:82px;height:82px;border:4px solid var(--white);border-radius:10px}
.brand-rule{position:absolute;left:187px;top:30px;width:4px;height:125px;background:var(--gold)}
.brand-name{position:absolute;left:215px;top:22px;font-family:"Oswald",sans-serif;font-weight:700;font-size:72px;line-height:1;letter-spacing:1px}
.brand-sub{position:absolute;left:216px;top:103px;font-family:"Oswald",sans-serif;font-weight:600;font-size:25px;letter-spacing:.5px;font-weight:600}
.brand-corp{position:absolute;left:216px;top:137px;font-size:17px;font-weight:500}
.location{position:absolute;left:685px;top:88px;display:flex;gap:10px;align-items:flex-start}
.location-text{font-size:18px;line-height:1.3;font-weight:500}
.location-text strong{color:var(--gold);font-weight:600}

.hero-photo{position:absolute;left:0;top:181px;width:928px;height:520px;
  background:linear-gradient(180deg,var(--sky) 0%,#d6e4ef 30%,var(--field) 40%,var(--road) 62%,#3a4456 80%,var(--navy) 100%)}

.headline{position:absolute;left:0;top:510px;width:928px;text-align:center;z-index:2}
.headline-top{display:block;font-family:"Anton",sans-serif;font-size:106px;line-height:1;letter-spacing:.5px;color:var(--white)}
.headline-bottom{display:block;margin-top:2px;font-family:"Archivo",sans-serif;font-stretch:125%;font-weight:900;font-size:84px;line-height:1;letter-spacing:5px;color:var(--gold)}

.tagline{position:absolute;left:50px;top:711px;width:828px;display:flex;align-items:center;gap:14px;font-size:20px;font-weight:600}
.tagline::before,.tagline::after{content:"";flex:1;height:2px;background:var(--gold)}

.concentrations{position:absolute;left:55px;top:752px}
.conc-title{position:absolute;left:0;top:0;width:820px;text-align:center;font-size:22px;font-weight:700;color:var(--ink);line-height:28px;top:8px}
.conc-grid{position:absolute;left:0;top:48px;width:820px;display:flex}
.conc-item{flex:1;text-align:center;color:var(--ink);position:relative}
.conc-item+.conc-item{border-left:2px solid #5b6475}
.conc-value{font-family:"Archivo",sans-serif;font-stretch:125%;font-weight:900;font-size:72px;line-height:.95}
.conc-value small{font-size:44px}
.conc-rule{width:170px;height:2px;background:var(--gold);margin:6px auto 6px}
.conc-label{font-size:20px;font-weight:500;line-height:1.22}

.services{position:absolute;left:55px;top:975px;width:816px;height:55px;border:3px solid var(--gold);border-radius:8px;background:var(--panel);display:flex;align-items:center;justify-content:center;gap:18px;color:var(--ink);font-family:"Oswald",sans-serif;font-weight:600;font-size:24px;letter-spacing:.3px}
.services .dot{width:8px;height:8px;border-radius:50%;background:var(--gold)}
.services .icon-left{position:absolute;left:34px;top:10px}
.services .icon-right{position:absolute;right:20px;top:10px}

.province-map{position:absolute;left:113px;top:1039px;width:64px;height:62px;background:var(--gold);border-radius:6px}
.reach{position:absolute;left:200px;top:1050px;width:600px;text-align:center;font-size:23px;font-weight:700;line-height:1.17}
.reach em{font-style:normal;color:var(--gold)}

.divider{position:absolute;left:47px;top:1118px;width:834px;height:1px;background:#3a4a6a}
.contact{position:absolute;top:1133px;height:48px;display:flex;align-items:center;gap:16px}
.contact-phone{left:70px}
.contact-email{left:474px}
.contact-badge{width:44px;height:44px;border-radius:50%;background:var(--gold);display:flex;align-items:center;justify-content:center}
.contact-phone .contact-text{font-size:42px;font-weight:700}
.contact-email .contact-text{font-size:26px;font-weight:600}
.contact-sep{position:absolute;left:446px;top:1133px;width:2px;height:44px;background:var(--gold)}
</style>
</head>
<body>
<main class="ad">
  <header class="header">
    <svg class="header-corner" width="80" height="70" viewBox="0 0 80 70"><polygon points="0,0 80,0 80,70" fill="var(--navy-mid)"/></svg>
    <div class="brand-mark"></div>
    <div class="brand-rule"></div>
    <div class="brand-name">MARWICK</div>
    <div class="brand-sub">DUST CONTROL PRODUCTS</div>
    <div class="brand-corp">418307 Ontario Limited</div>
    <div class="location">
      <svg width="26" height="38" viewBox="0 0 26 38"><path d="M13 1C6.4 1 1 6.2 1 12.8 1 21.5 13 34 13 34S25 21.5 25 12.8C25 6.2 19.6 1 13 1z" fill="var(--gold)"/><circle cx="13" cy="12.5" r="4.6" fill="var(--navy)"/><ellipse cx="13" cy="36" rx="6" ry="1.6" fill="var(--gold)"/></svg>
      <div class="location-text">Based in<br><strong>Clinton, Ontario</strong></div>
    </div>
  </header>

  <div class="hero-photo" role="img" aria-label="Tanker truck spraying liquid dust suppressant on a gravel rural road between crop fields under a blue sky"></div>

  <h1 class="headline">
    <span class="headline-top">ROAD DUST CONTROL</span>
    <span class="headline-bottom">PRODUCTS</span>
  </h1>

  <p class="tagline">Manufacturer &amp; Distributor of Liquid Road Dust Suppressants</p>

  <section class="concentrations">
    <svg width="820" height="208" viewBox="0 0 820 208">
      <polygon points="20,22 200,22 225,0 595,0 620,22 800,22 820,42 820,188 800,208 20,208 0,188 0,42" fill="var(--panel)"/>
    </svg>
    <h2 class="conc-title">AVAILABLE CONCENTRATIONS</h2>
    <div class="conc-grid">
      <div class="conc-item"><div class="conc-value">35<small>%</small></div><div class="conc-rule"></div><div class="conc-label">Liquid Calcium<br>Magnesium<br>Chloride Solution</div></div>
      <div class="conc-item"><div class="conc-value">30<small>%</small></div><div class="conc-rule"></div><div class="conc-label">Liquid Calcium<br>Magnesium<br>Chloride Solution</div></div>
      <div class="conc-item"><div class="conc-value">20<small>%</small></div><div class="conc-rule"></div><div class="conc-label">Liquid Calcium<br>Magnesium<br>Chloride Solution</div></div>
    </div>
  </section>

  <div class="services">
    <svg class="icon-left" width="24" height="32" viewBox="0 0 24 32"><path d="M12 1C12 1 2 14 2 21a10 10 0 0 0 20 0C22 14 12 1 12 1z" fill="var(--navy-mid)"/></svg>
    <span>BULK SUPPLY</span><span class="dot"></span><span>DELIVERY</span><span class="dot"></span><span>ROAD APPLICATION</span>
    <svg class="icon-right" width="96" height="32" viewBox="0 0 96 32"><rect x="2" y="6" width="52" height="16" rx="7" fill="none" stroke="var(--ink)" stroke-width="3"/><path d="M56 10h10l7 8v6H56z" fill="var(--ink)"/><rect x="2" y="22" width="72" height="3" fill="var(--ink)"/><circle cx="14" cy="27" r="4" fill="var(--ink)"/><circle cx="26" cy="27" r="4" fill="var(--ink)"/><circle cx="64" cy="27" r="4" fill="var(--ink)"/><g fill="var(--ink)"><circle cx="80" cy="14" r="1.3"/><circle cx="85" cy="10" r="1.3"/><circle cx="85" cy="18" r="1.3"/><circle cx="90" cy="7" r="1.3"/><circle cx="90" cy="14" r="1.3"/><circle cx="90" cy="21" r="1.3"/></g></svg>
  </div>

  <div class="province-map" role="img" aria-label="Map of Ontario"></div>
  <p class="reach">SUPPLYING MUNICIPALITIES, CONTRACTORS &amp;<br>COMMERCIAL CUSTOMERS <em>ACROSS ONTARIO</em></p>

  <div class="divider"></div>
  <div class="contact contact-phone">
    <span class="contact-badge"><svg width="24" height="24" viewBox="0 0 24 24"><path d="M6.6 10.8a15 15 0 0 0 6.6 6.6l2.2-2.2a1 1 0 0 1 1-.25 11.4 11.4 0 0 0 3.6.57 1 1 0 0 1 1 1V20a1 1 0 0 1-1 1A17 17 0 0 1 3 4a1 1 0 0 1 1-1h3.5a1 1 0 0 1 1 1c0 1.25.2 2.45.57 3.57a1 1 0 0 1-.25 1z" fill="var(--navy)"/></svg></span>
    <span class="contact-text">519-555-0187</span>
  </div>
  <div class="contact-sep"></div>
  <div class="contact contact-email">
    <span class="contact-badge"><svg width="24" height="18" viewBox="0 0 24 18"><rect x="1.5" y="1.5" width="21" height="15" rx="2" fill="none" stroke="var(--navy)" stroke-width="2.2"/><path d="M2 3l10 7 10-7" fill="none" stroke="var(--navy)" stroke-width="2.2"/></svg></span>
    <span class="contact-text">dermarw417@quillpost.net</span>
  </div>
</main>
</body>
</html>
```